Meetup group needs an awesome poster

We need a poster to advertise our local meetup group for embedded systems engineers. This poster will be sent to various technology companies in Auckland, New Zealand to recruit new members.
http://www.gathervine.net/Auckland-Circuit-Tinkerers-Club/
Embedded systems engineers design electronic circuits, and design software for micro-controllers.
Target Market(s)
Embedded Systems Engineers
Industry/Entity Type
Group
Font styles to use
Other font styles liked:
- Console
Requirements
Must have
- Information about the meetup group:
- Monthly meetups
- 1-2 presentations from the community
- Optional time for socialising over a few drinks at a local spot
- Hosted at tech companies around Auckland.
Nice to have
- Funny or quirky imagery

```html
<!DOCTYPE html>
<html lang="en">
<head>
<meta charset="utf-8">
<title>Auckland Embedded Systems meet-up</title>
<link rel="stylesheet" href="https://fonts.googleapis.com/css2?family=Open+Sans:wght@600;700&display=swap">
<style>
  :root {
    --board-deep: #050a0c;
    --board-mid: #0b1a20;
    --trace-teal: #1f4f5a;
    --trace-blue: #1d3f5c;
    --label-bg: #3b7083;
    --label-ink: #ffffff;
    --tag-ink: #050505;
  }
  * { margin: 0; padding: 0; box-sizing: border-box; }
  html, body {
    width: 927px;
    height: 1200px;
    overflow: hidden;
    background: var(--board-deep);
  }
  .poster {
    position: relative;
    width: 927px;
    height: 1200px;
    overflow: hidden;
    font-family: "Open Sans", Arial, sans-serif;
  }
  .circuit-backdrop {
    position: absolute;
    inset: 0;
    background:
      radial-gradient(ellipse at 15% 30%, var(--trace-teal) 0%, transparent 45%),
      radial-gradient(ellipse at 80% 75%, var(--trace-blue) 0%, transparent 50%),
      radial-gradient(ellipse at 30% 90%, var(--trace-teal) 0%, transparent 40%),
      linear-gradient(160deg, var(--board-mid) 0%, var(--board-deep) 55%, var(--board-mid) 100%);
  }
  .title-stack { position: absolute; inset: 0 0 auto 0; height: 710px; }
  .title-line {
    position: absolute;
    right: 0;
    display: flex;
    align-items: center;
    justify-content: flex-end;
    background: var(--label-bg);
    color: var(--label-ink);
    font-weight: 600;
    font-size: 114px;
    line-height: 1;
    letter-spacing: 0;
    padding-right: 34px;
    white-space: nowrap;
  }
  .title-line--city    { top: 77px;  left: 235px; height: 139px; }
  .title-line--field   { top: 247px; left: 235px; height: 139px; }
  .title-line--systems { top: 412px; left: 360px; height: 139px; }
  .title-line--tag {
    top: 587px;
    left: 450px;
    height: 113px;
    color: var(--tag-ink);
    font-weight: 700;
    font-size: 100px;
    padding-bottom: 14px;
  }
  .meetup-details {
    position: absolute;
    top: 770px;
    right: 0;
    display: flex;
    flex-direction: column;
    align-items: flex-end;
    gap: 16px;
    list-style: none;
  }
  .detail {
    background: var(--label-bg);
    color: var(--label-ink);
    font-weight: 600;
    font-size: 38px;
    line-height: 1;
    padding: 14px 34px 16px 28px;
    white-space: nowrap;
  }
  .detail--link {
    margin-top: 14px;
    font-size: 24px;
    color: var(--tag-ink);
    font-weight: 700;
  }
</style>
</head>
<body>
  <main class="poster">
    <div class="circuit-backdrop" role="img" aria-label="Dark collage of glowing teal and blue circuit-board traces"></div>
    <h1 class="title-stack">
      <span class="title-line title-line--city">AUCKLAND</span>
      <span class="title-line title-line--field">EMBEDDED</span>
      <span class="title-line title-line--systems">SYSTEMS</span>
      <span class="title-line title-line--tag">meet-up</span>
    </h1>
    <ul class="meetup-details">
      <li class="detail">Monthly meetups</li>
      <li class="detail">1–2 talks from the community</li>
      <li class="detail">Optional drinks at a local spot</li>
      <li class="detail">Hosted at Auckland tech companies</li>
      <li class="detail detail--link">www.gathervine.net/Auckland-Circuit-Tinkerers-Club/</li>
    </ul>
  </main>
</body>
</html>
```